Psychotherapy Website - Based in London

I am a newly trained psychotherapist and need a new website for www.rosalindfaber.co.uk.

I offer therapy for addiction, relationships, trauma and many other issues people face in their lives.

I want the website to be welcoming, gentle, feminine and for people to feel safe.

I do not like a page site that scrolls through sections, rather each page should be separate. Here some examples that i like. Sectional rather than scrolled.

https://www.hettiemarsh.com/
https://www.thequietwardrooms.com/

The imagery should be around pink using the flower in the logo / wording and around the site:

Here is a link to the flower for ideas:
https://www.pictofind.net/search?q=pink+gerbera&rlz=2D4KQTW_en-GBGB415GB415&source=lnms&tbm=isch&sa=X&ved=7cvQRtrk482h3PxZTuKLmeNBwXW_1AtXpVlKDbOQBmFLB&biw=1500&bih=889&dpr=2

RosalindFaber
Compassionate Psychotherapy

Is the logo and subheader for the website. Please use a typeface for the name that is appealing and professional.

Type face similar NOT EXLUSIVLY - JUST AN IDEA like this:
https://glowtonicstudio.com/

Basic business card i created as a rough idea below.

I have also added the website copy.

The headers are

Homepage
About Me
Therapy
Common Questions
Blog
Contact Me

Target Market(s)

Clients who are dealing with stress, trauma, pain, addiction

Industry/Entity Type

Therapy and Psychology

Coding

Coded - Design and coding required

Number of Pages Required

5+ page

Font styles to use
Serif
Sans Serif
Script

Colors
0054AA
0677BA
7BADD7
CADEEF
E8F1F8
0094D4
00A9DD
6FCCEA
C7EBF8
E9F6FB
E54698
E96AAD
F1A4CE
F9D9EA
FCEFF6

Requirements
Must have
• Pink Gerbera Flower integrated into design
Nice to have
• Images but not to stock imagery. Needs to look authentic and natural
Should not have
• Stock images of people. Images are important but needs to feel REAL

```html
<!DOCTYPE html>
<html lang="en">
<head>
<meta charset="utf-8">
<title>Rosalind Faber – Compassionate Psychotherapy</title>
<link href="https://fonts.googleapis.com/css2?family=Playfair+Display:wght@400;700&family=Jost:wght@400;500;600&display=swap" rel="stylesheet">
<style>
:root{
  --blue-deep:#0054AA;
  --blue:#0677BA;
  --blue-mid:#0094D4;
  --blue-bright:#00A9DD;
  --blue-soft:#6FCCEA;
  --blue-pale:#E9F6FB;
  --pink:#E54698;
  --pink-mid:#E96AAD;
  --pink-soft:#F1A4CE;
  --pink-pale:#F9D9EA;
  --pink-mist:#FCEFF6;
  --ink:#333;
  --grey:#888;
}
*{margin:0;padding:0;box-sizing:border-box}
html,body{width:1200px;height:3969px;overflow:hidden}
body{position:relative;background:#fff;font-family:"Jost",sans-serif;color:var(--ink)}
h1,h2,h3,h4,h5{font-weight:400}
a{text-decoration:none}
.abs{position:absolute}
.serif{font-family:"Playfair Display",serif}

/* header */
.site-header{left:0;top:0;width:1200px;height:86px;background:#fff;z-index:5}
.brand{left:120px;top:14px}
.brand-name{font-size:27px;color:var(--blue-mid);letter-spacing:.5px;line-height:1}
.brand-name b{font-weight:600}
.brand-tag{font-size:15px;color:var(--blue-mid);margin-top:5px}
.main-nav{left:412px;top:34px;display:flex;gap:40px;font-size:14px;text-transform:uppercase}
.main-nav a{color:#222}
.main-nav a.active{color:var(--pink);position:relative}
.main-nav a.active::after{content:"";position:absolute;left:0;right:0;bottom:-12px;height:2px;background:var(--blue-mid)}

/* hero */
.hero{left:0;top:86px;width:1200px;height:620px;overflow:hidden}
.hero-photo{position:absolute;inset:0;background:radial-gradient(ellipse at 50% 30%,#f9a6cf 0%,#ee5fa4 45%,#e23e8f 100%)}
.hero-title{left:0;top:168px;width:1200px;text-align:center;color:#fff;font-size:58px;line-height:62px;text-transform:uppercase;font-weight:400}
.hero-sub{left:0;top:298px;width:1200px;text-align:center;color:#fff;font-size:22px;letter-spacing:.5px}
.btn{display:inline-block;color:#fff;font-weight:600;font-size:16px;text-transform:uppercase;text-align:center;border-radius:0 22px 0 22px}
.btn-blue{background:linear-gradient(90deg,var(--blue) 0%,var(--blue-soft) 100%)}
.btn-pink{background:linear-gradient(90deg,var(--pink) 0%,var(--pink-soft) 100%)}
.hero-btn{left:504px;top:342px;width:186px;height:54px;line-height:54px}
.hero-wave{left:0;top:520px}

/* welcome */
.welcome{left:0;top:796px;width:1200px;height:502px;background:linear-gradient(90deg,#fff 0%,var(--pink-mist) 50%,#fff 100%)}
.welcome-title{left:145px;top:30px;font-size:38px;line-height:45px;text-transform:uppercase;color:var(--blue-mid)}
.welcome-title span{color:var(--pink);font-weight:700}
.rule{width:60px;height:3px;display:flex;gap:5px}
.rule i{display:block;height:3px}
.rule i:first-child{width:38px;background:var(--blue-mid)}
.rule i:last-child{width:12px;background:var(--pink)}
.welcome .rule{left:145px;top:130px}
.welcome-copy{left:145px;top:156px;width:440px;font-size:13.2px;line-height:23px;color:#333}
.welcome-copy p+p{margin-top:8px}
.welcome-flower{left:618px;top:14px;width:582px;height:488px;background:radial-gradient(circle at 48% 32%,#f6c3dc 0%,#ee7db6 26%,#f6d4e6 45%,rgba(255,255,255,0) 62%)}

/* practice */
.practice{left:0;top:1297px;width:1200px;height:570px}
.frame{left:158px;top:89px;width:310px;height:312px;border:2px solid #fff}
.portrait{left:171px;top:100px;width:346px;height:350px;background:linear-gradient(180deg,#e8e4df 0%,#e1c8b8 55%,#e86aa8 100%)}
.practice-title{left:583px;top:113px;font-size:38px;color:#fff;text-transform:uppercase}
.practice-title b{font-weight:700}
.practice .rule{left:583px;top:170px}
.practice .rule i:first-child{background:#fff}
.practice .rule i:last-child{background:#fff;opacity:.8}
.practice-copy{left:583px;top:191px;width:480px;color:#fff;font-size:15px;line-height:24.5px}
.practice-copy p+p{margin-top:8px}
.practice-btn{left:585px;top:399px;width:176px;height:50px;line-height:50px;font-size:15px}

/* therapy areas */
.areas-title{left:0;top:1910px;width:1200px;text-align:center;font-size:33px;color:var(--blue-mid);text-transform:uppercase}
.areas-title b{color:var(--pink);font-weight:700}
.areas-rule{left:567px;top:1960px}
.center-ring{left:428px;top:2068px;width:340px;height:340px;border:2px solid var(--blue-soft);border-radius:50%}
.center-flower{left:443px;top:2083px;width:310px;height:310px;border-radius:50%;background:radial-gradient(circle,#f9c6df 0%,#ef72b1 55%,#e6509d 100%)}
.node{width:12px;height:12px;border:3px solid var(--pink-mid);background:#fff;border-radius:50%}
.area-icon{width:70px;height:70px;border-radius:50%}
.area-icon svg{display:block;margin:17px auto}
.ic-blue{background:var(--blue)}
.ic-pink{background:var(--pink)}
.ic-sky{background:var(--blue-soft)}
.area h3{font-size:16px;font-weight:600;text-transform:uppercase;color:#222}
.area p{font-size:10.5px;line-height:16px;color:var(--grey);margin-top:3px}
.area.left{text-align:right}

/* why */
.why{left:0;top:2505px;width:1200px;height:466px;background:linear-gradient(180deg,#1463c4 0%,#0b5ab6 55%,#0a4f9f 100%)}
.why-title{left:0;top:95px;width:1200px;text-align:center;color:#fff;font-size:38px;text-transform:uppercase}
.why-title b{font-weight:700}
.why .rule{left:570px;top:150px}
.why .rule i{background:#fff}
.why-copy{left:250px;top:183px;width:700px;text-align:center;color:#fff;font-size:18.5px;line-height:32px}
.why-btn{left:511px;top:292px;width:182px;height:52px;line-height:52px}

/* blogs */
.blogs-title{left:0;top:3022px;width:1200px;text-align:center;font-size:34px;color:var(--blue-mid);text-transform:uppercase}
.blogs-title b{color:var(--pink);font-weight:700}
.blogs-rule{left:579px;top:3075px}
.blog-card{top:3107px;width:305px;height:365px;background:#fff;box-shadow:0 2px 10px rgba(0,0,0,.08)}
.blog-img{height:203px}
.blog-body{padding:25px 34px}
.blog-body h4{font-size:15px;font-weight:600;line-height:22px;color:#222}
.blog-body p{font-size:12px;line-height:21px;color:var(--grey);margin-top:8px}
.blog-body a{display:block;margin-top:6px;font-size:12px;font-weight:600;color:var(--pink)}

/* footer */
.footer-wave{left:0;top:3505px}
.site-footer{left:0;top:3600px;width:1200px;height:369px;background:linear-gradient(180deg,var(--pink) 0%,var(--pink-mid) 60%,var(--pink-soft) 100%)}
.foot-brand{left:145px;top:73px;color:#fff}
.foot-brand .brand-name{color:#fff;font-size:29px}
.foot-brand .brand-tag{color:#fff;font-size:15px}
.social{left:148px;top:160px;display:flex;gap:6px}
.social span{width:38px;height:38px;border-radius:50%;border:2px solid #fff;display:block}
.foot-col{top:80px;color:#fff}
.foot-col h5{font-size:19px;font-weight:500;margin-bottom:10px}
.foot-col li{list-style:none;font-size:14px;line-height:25px;padding-left:2px}
.copyright{left:0;top:322px;width:1200px;text-align:center;font-size:12px;color:#fff;border-top:1px solid rgba(255,255,255,.25);padding-top:14px}
</style>
</head>
<body>

<header class="site-header abs">
  <div class="brand abs">
    <div class="brand-name"><b>ROSALIND</b>FABER</div>
    <div class="brand-tag">Compassionate Psychotherapy</div>
  </div>
  <nav class="main-nav abs">
    <a class="active" href="#">Home</a>
    <a href="#">About Me</a>
    <a href="#">Therapy</a>
    <a href="#">Common Questions</a>
    <a href="#">Blog</a>
    <a href="#">Contact Me</a>
  </nav>
</header>

<section class="hero abs">
  <div class="hero-photo" role="img" aria-label="Close-up of pink gerbera petals with a water droplet"></div>
  <h1 class="hero-title abs serif">Recovery from<br>stress &amp; depression</h1>
  <div class="hero-sub abs">COMPASSIONATE PSYCHOTHERAPY</div>
  <a class="btn btn-blue hero-btn abs" href="#">Contact Me</a>
  <svg class="abs" style="left:587px;top:492px" width="26" height="50" viewBox="0 0 26 50" fill="none" stroke="#fff" stroke-width="1.6">
    <rect x="6" y="1" width="14" height="24" rx="7"/><line x1="13" y1="6" x2="13" y2="11"/>
    <polyline points="8,32 13,37 18,32"/><polyline points="8,39 13,44 18,39"/>
  </svg>
  <svg class="hero-wave abs" width="1200" height="100" viewBox="0 0 1200 100" preserveAspectRatio="none">
    <path d="M0 40 C200 95 380 100 600 70 C820 40 1000 55 1200 0 L1200 100 L0 100Z" fill="#fff"/>
    <path d="M0 40 C200 95 380 100 600 70 C820 40 1000 55 1200 0" stroke="#E54698" stroke-width="4" fill="none"/>
  </svg>
</section>

<section class="welcome abs">
  <h2 class="welcome-title abs serif">Welcome to<br><span>Rosalind Faber</span></h2>
  <div class="rule abs"><i></i><i></i></div>
  <div class="welcome-copy abs">
    <p>Taking the first steps towards engaging in therapy can be a very personal journey. Whilst, it can be challenging, I will ensure to make this journey as safe and as comfortable for you as possible.</p>
    <p>Psychotherapy can help you see your current situation in new light, depth and clarity. It can change old and unhelpful perspectives and feelings about yourself and your life, and ultimately help you make positive changes. It might be the most important journey you’ll ever make. I provide a and non-judgmental space where any issues can be explored in complete confidentiality.</p>
  </div>
  <div class="welcome-flower abs" role="img" aria-label="Single pink gerbera flower on a green stem"></div>
</section>

<section class="practice abs">
  <svg class="abs" style="left:0;top:0" width="1200" height="570" viewBox="0 0 1200 570" preserveAspectRatio="none">
    <defs><linearGradient id="practiceBg" x1="0" y1="0" x2="1" y2="0"><stop offset="0" stop-color="#0677BA"/><stop offset=".5" stop-color="#2C9FDB"/><stop offset="1" stop-color="#6FCCEA"/></linearGradient></defs>
    <path d="M0 0 H1200 V495 C1050 545 900 520 700 520 C500 520 350 590 160 560 C90 548 40 530 0 505Z" fill="url(#practiceBg)"/>
    <path d="M0 505 C40 530 90 548 160 560 C350 590 500 520 700 520 C900 520 1050 545 1200 495" stroke="#E54698" stroke-width="5" fill="none"/>
  </svg>
  <div class="frame abs"></div>
  <div class="portrait abs" role="img" aria-label="Portrait photograph of the therapist"></div>
  <svg class="abs" style="left:325px;top:300px" width="215" height="170" viewBox="0 0 215 170" fill="#fff">
    <g opacity=".8">
      <circle cx="195" cy="5" r="1.5"/><circle cx="205" cy="5" r="1.5"/><circle cx="195" cy="20" r="1.5"/><circle cx="205" cy="20" r="1.5"/>
      <circle cx="195" cy="35" r="1.5"/><circle cx="205" cy="35" r="1.5"/><circle cx="195" cy="50" r="1.5"/><circle cx="205" cy="50" r="1.5"/>
      <circle cx="195" cy="65" r="1.5"/><circle cx="205" cy="65" r="1.5"/><circle cx="195" cy="80" r="1.5"/><circle cx="205" cy="80" r="1.5"/>
      <circle cx="195" cy="95" r="1.5"/><circle cx="205" cy="95" r="1.5"/><circle cx="195" cy="110" r="1.5"/><circle cx="205" cy="110" r="1.5"/>
      <circle cx="195" cy="125" r="1.5"/><circle cx="205" cy="125" r="1.5"/>
      <circle cx="10" cy="155" r="1.5"/><circle cx="25" cy="155" r="1.5"/><circle cx="40" cy="155" r="1.5"/><circle cx="55" cy="155" r="1.5"/><circle cx="70" cy="155" r="1.5"/><circle cx="85" cy="155" r="1.5"/><circle cx="100" cy="155" r="1.5"/><circle cx="115" cy="155" r="1.5"/><circle cx="130" cy="155" r="1.5"/><circle cx="145" cy="155" r="1.5"/><circle cx="160" cy="155" r="1.5"/><circle cx="175" cy="155" r="1.5"/><circle cx="190" cy="155" r="1.5"/><circle cx="205" cy="155" r="1.5"/>
      <circle cx="10" cy="165" r="1.5"/><circle cx="25" cy="165" r="1.5"/><circle cx="40" cy="165" r="1.5"/><circle cx="55" cy="165" r="1.5"/><circle cx="70" cy="165" r="1.5"/><circle cx="85" cy="165" r="1.5"/><circle cx="100" cy="165" r="1.5"/><circle cx="115" cy="165" r="1.5"/><circle cx="130" cy="165" r="1.5"/><circle cx="145" cy="165" r="1.5"/><circle cx="160" cy="165" r="1.5"/><circle cx="175" cy="165" r="1.5"/><circle cx="190" cy="165" r="1.5"/><circle cx="205" cy="165" r="1.5"/>
    </g>
  </svg>
  <h2 class="practice-title abs serif">My <b>Practice</b></h2>
  <div class="rule abs"><i></i><i></i></div>
  <div class="practice-copy abs">
    <p>My practice is based in Ashbourne Vale, where the room is homely, comfortable and welcoming. I believe a good environment contributes to great therapy. &nbsp;Alternately, I am also available to provide therapy online, if this environment is more accommodating for my clients.</p>
    <p>I am passionate about improving mental health and committed to offering therapy to all individuals regardless of their age, race, culture, disability, sexual orientation, or socio-economic background.</p>
  </div>
  <a class="btn btn-pink practice-btn abs" href="#">Learn More</a>
</section>

<h2 class="areas-title abs serif">Therapy help <b>you to recover</b></h2>
<div class="rule areas-rule abs"><i></i><i></i></div>

<div class="center-ring abs"></div>
<div class="center-flower abs" role="img" aria-label="Pink gerbera flower head seen from above"></div>
<span class="node abs" style="left:505px;top:2085px"></span>
<span class="node abs" style="left:671px;top:2079px"></span>
<span class="node abs" style="left:427px;top:2189px"></span>
<span class="node abs" style="left:754px;top:2189px"></span>
<span class="node abs" style="left:444px;top:2317px"></span>
<span class="node abs" style="left:738px;top:2317px"></span>

<div class="area-icon ic-blue abs" style="left:438px;top:2024px"><svg width="36" height="36" viewBox="0 0 36 36" fill="none" stroke="#fff" stroke-width="2"><circle cx="18" cy="16" r="10"/><path d="M13 26 v6 M23 26 v6"/></svg></div>
<div class="area left abs" style="left:200px;top:2034px;width:218px"><h3>Addiction</h3><p>Lorem Ipsum is simply dummy text of<br>the printing and typesetting.</p></div>

<div class="area-icon ic-blue abs" style="left:695px;top:2028px"><svg width="36" height="36" viewBox="0 0 36 36" fill="none" stroke="#fff" stroke-width="2"><circle cx="18" cy="16" r="10"/><path d="M14 18 q4 3 8 0"/></svg></div>
<div class="area abs" style="left:780px;top:2030px;width:220px"><h3>Fear</h3><p>Lorem Ipsum is simply dummy text of<br>the printing and typesetting.</p></div>

<div class="area-icon ic-pink abs" style="left:348px;top:2154px"><svg width="36" height="36" viewBox="0 0 36 36" fill="none" stroke="#fff" stroke-width="2"><circle cx="18" cy="16" r="10"/><path d="M14 20 q4 -3 8 0"/></svg></div>
<div class="area left abs" style="left:120px;top:2162px;width:216px"><h3>Depression</h3><p>Lorem Ipsum is simply dummy text of<br>the printing and typesetting.</p></div>

<div class="area-icon ic-pink abs" style="left:780px;top:2154px"><svg width="36" height="36" viewBox="0 0 36 36" fill="none" stroke="#fff" stroke-width="2"><circle cx="18" cy="16" r="10"/><path d="M12 12 l12 8 M24 12 l-12 8"/></svg></div>
<div class="area abs" style="left:865px;top:2160px;width:220px"><h3>Stress</h3><p>Lorem Ipsum is simply dummy text of<br>the printing and typesetting.</p></div>

<div class="area-icon ic-sky abs" style="left:366px;top:2303px"><svg width="36" height="36" viewBox="0 0 36 36" fill="none" stroke="#fff" stroke-width="2"><circle cx="18" cy="16" r="10"/><path d="M18 10 v8"/></svg></div>
<div class="area left abs" style="left:130px;top:2313px;width:218px"><h3>Anxiety</h3><p>Lorem Ipsum is simply dummy text of<br>the printing and typesetting.</p></div>

<div class="area-icon ic-sky abs" style="left:760px;top:2303px"><svg width="36" height="36" viewBox="0 0 36 36" fill="none" stroke="#fff" stroke-width="2"><path d="M18 30 L6 18 a6 6 0 0 1 12 -8 a6 6 0 0 1 12 8Z"/><path d="M6 19 h7 l2 -4 l3 7 l2 -3 h10"/></svg></div>
<div class="area abs" style="left:843px;top:2313px;width:220px"><h3>Health Issues</h3><p>Lorem Ipsum is simply dummy text of<br>the printing and typesetting.</p></div>

<section class="why abs" role="img" aria-label="Misty blue forest and hills">
  <h2 class="why-title abs serif">Why our <b>Therapy</b></h2>
  <div class="rule abs"><i></i><i></i></div>
  <p class="why-copy abs">Lorem ipsum dolor sit amet, consectetur adipiscing elit, sed do eiusmod tempor incididunt ut labore et dolore magna aliqua. Ut enim ad minim veniam, quis nostrud exercitation ullamco laboris ni</p>
  <a class="btn btn-pink why-btn abs" href="#">Learn More</a>
</section>

<h2 class="blogs-title abs serif">Our latest <b>Blogs</b></h2>
<div class="rule blogs-rule abs"><i></i><i></i></div>

<article class="blog-card abs" style="left:138px">
  <div class="blog-img" role="img" aria-label="Stacked grey pebbles on raked sand" style="background:linear-gradient(135deg,#e7e7e7,#a9a9a9)"></div>
  <div class="blog-body"><h4>Lorem ipsum dolor sit amet, consectetur adipiscing</h4><p>Excepteur sint occaecat cupidatat non proident, sunt in culpa qui</p><a href="#">Learn More →</a></div>
</article>
<article class="blog-card abs" style="left:465px">
  <div class="blog-img" role="img" aria-label="Balanced stones on a beach at sunset" style="background:linear-gradient(180deg,#dcb894,#a0836c 60%,#6f6664)"></div>
  <div class="blog-body"><h4>Lorem ipsum dolor sit amet, consectetur adipiscing</h4><p>Excepteur sint occaecat cupidatat non proident, sunt in culpa qui</p><a href="#">Learn More →</a></div>
</article>
<article class="blog-card abs" style="left:792px">
  <div class="blog-img" role="img" aria-label="Mountain meadow of pink flowers at sunrise" style="background:linear-gradient(180deg,#5e4f8a,#e2a05b 35%,#4a5a8c 60%,#c24a8e)"></div>
  <div class="blog-body"><h4>Lorem ipsum dolor sit amet, consectetur adipiscing</h4><p>Excepteur sint occaecat cupidatat non proident, sunt in culpa qui</p><a href="#">Learn More →</a></div>
</article>

<svg class="footer-wave abs" width="1200" height="100" viewBox="0 0 1200 100" preserveAspectRatio="none">
  <defs><linearGradient id="swoosh" x1="0" y1="0" x2="1" y2="0"><stop offset="0" stop-color="#0677BA"/><stop offset="1" stop-color="#6FCCEA"/></linearGradient></defs>
  <path d="M0 0 C250 40 450 45 600 45 C800 45 1000 35 1200 0 V100 H0Z" fill="#E54698"/>
  <path d="M170 55 C400 92 800 92 1020 55 C800 108 400 108 170 55Z" fill="url(#swoosh)"/>
</svg>

<footer class="site-footer abs">
  <div class="foot-brand abs">
    <div class="brand-name"><b>ROSALIND</b> FABER</div>
    <div class="brand-tag">Compassionate Psychotherapy</div>
  </div>
  <div class="social abs"><span></span><span></span><span></span><span></span></div>
  <div class="foot-col abs" style="left:501px">
    <h5>Quick links</h5>
    <ul><li>About Me</li><li>Therapy</li><li>Common Questions</li><li>Blog</li><li>Contact Me</li></ul>
  </div>
  <div class="foot-col abs" style="left:753px">
    <h5>Contact</h5>
    <ul><li>Willowmere Community Centre</li><li>27 Fenwick Lane Ashbourne Vale AV4 7QX</li><li>rosalind@kindredcounsel.example</li><li>07700 900418</li></ul>
  </div>
  <div class="copyright abs">Copyright © 2021 Rosalind Faber</div>
</footer>

</body>
</html>
```